依頼詳細
全体のイメージは、キャッチとサブキャッチをメインに講義の内容がわかり易く
セミナーへ来たくなるような興味を惹く、斬新なデザインでお願いします。
注意:講演タイトルや日時を大きく協調される方が多いですが、それは避けてください。
また、イメージとして、協会や会社のHPを記載しておきますので参考にしてください。
・一般社団法人蒼岳地層調査会  https://kvrt-example.or.jp/
・株式会社R-VANTLO  https://rvantlo-example.co.jp/
以前に作っていただいたサンプルチラシがありますが、あまりにも普通なデザインでしたので、悪い事例として添付しておきます。こんなデザインは避けてください。(PPTデータ)
講師の写真データもPPTに入っています。

講師
浦辺 直孝 ※写真入
蒼洋材料技術機構 主幹研究員/博士(工学)
複層素材耐久分析部門 兼 湾岸フロンティア計測センター 主幹研究員
2017年4月9日TVRドキュメント「森の湖 あの町はどこへ?~消えゆく“水辺の記憶”~」新聞・雑誌等掲載多数
講演タイトル「地震大国に必要とされるハイブリット微動探査の将来性」

宮下 航  ※写真入
株式会社Tk’s空間計画 代表取締役社長 「匠研舎」塾長
一級建築士、一級構造建築士 専門は木造構造建築物の構造設計・構造計算
工務店を経て、2006年5月㈱Tk‘s空間計画を設立、2010年1月「匠研舎」を設立し、木質構造に関するセミナーや構造計算技術者育成を行っている。現在は「匠研舎」の講座をweb化した「匠研舎チャンネル」、Cliporaにて情報発信中。著書に「すっきり学べる!石積み読本」がある
講演タイトル「地盤の揺れやすさを知った家づくりの重要性」

主催
株式会社R-VANTLO
〒471-0835愛知県名古屋市中区桜庭二丁目8番4号‐705号
URL:https://rvantlo-example.co.jp/

協賛
・一般社団法人蒼岳地層調査会 ・一般社団法人ソルベン ・株式会社タカミネ

問い合わせ
株式会社R-VANTLO 担当 村瀬 080-2938-6074
murase-hideaki@rvantlo-example.co.jp

記載項目
以下の『』内の文章を入れて下さい。
・セミナータイトル『最新工務店戦略・地盤の揺れやすさを知って地震に備えた家づくり』
・キャッチコピー『揺れにくい地盤には 価値がある』
・サブキャッチ『地盤の揺れやすさは、 今までの地盤測定方法では 計測出来ませんでした』
・セミナースケジュール
『日時:6月23日(水) 14:00~16:00(受付開始13:30)
場所:刈谷市中央障害学習センター5階(501~503)
定員:50名
同時 LIVE配信での開催(Vidora利用)』
・『来場者特典:当日会場に来ていただいた方には、初回調査を来場者特別価格にてご提供』
・講師名 写真入り 略歴 講演タイトルをそれぞれ入れて下さい。(依頼詳細参照)
・主催、協賛、問い合わせも入れて下さい。(依頼詳細参照)
※参加申込み欄の作成をお願いします。
『会社名、住所、参加者名、部署名、役職名、TEL、FAX、E-mail、参加人数、参加方法、現地かWEB』
・『WEBでご参加の場合はE-mailを必ずご記入下さい。』
・『会場入場前にご名刺を1枚頂戴いたしますのでご準備ください。』

サイズ
A4
ページ数
片面
希望イメージ
シンプル 複雑
単色 カラフル
暗い 明るい
日常 高級
遊び心 厳粛
未来的 伝統的
女性的 男性的
希望する色
設定なし
納品ファイル
• 高解像度JPG (.jpg)
• イラストレーター形式 (.ai)
• フォトショップ形式 (.psd)
補足説明
.ai形式はオリジナル&アウトライン化したものをください。イラストレーターのバージョンをCS6でお願いします。
.pdf(高解像度)をください。
チラシ内で使った画像を別途ください。
申込方法にWEB(Googleフォーム)も追加して下さい。
QRコードを添付しましたので宜しくお願い致します。
■ 選んだ理由

選ばせていただいた理由は、他の提案に比べて、圧倒的にインパクトでした。今回は折込チラシではなく、手渡しがメインのため、デザインや構図が一般的なものは外させていただきました。また、こちらの要望をよく把握されていない方もいらっしゃったようで、そのような提案も外させていただきました。
当選させていただいた提案は、使用する文字数が多い中、全体的に上手くまとめていただきまして、それでいて文字もしっかり目に入ってきて、こちらの要望にしっかりと応えてくれました、とても満足のいくものでした。

■ 提案者全員のお礼・コメント

コンペに応募していただいた皆様、本当にありがとうございました。当選された方以外にも、良い出来の提案が複数あり、最後まで悩み、当選と次点を選ばせていただきました。連絡が遅くなり申し訳ありませんでした。今回はこのような結果にさせていただきました。今後も定期的に依頼することがありますので、次回はまた、提案していただけると有難いです。今後とも宜しくお願い致します。

```html
<!DOCTYPE html>
<html lang="ja">
<head>
<meta charset="utf-8">
<title>最新工務店戦略 セミナー</title>
<link href="https://fonts.googleapis.com/css2?family=Noto+Sans+JP:wght@400;500;700;900&display=swap" rel="stylesheet">
<style>
:root{
  --green:#4cae3a;
  --green-light:#a9d68f;
  --green-pale:#e4f2da;
  --dark:#1f3a2c;
  --ink:#1b1b1b;
  --yellow:#f6d21d;
  --line:#6a6a6a;
  --paper:#ffffff;
}
*{margin:0;padding:0;box-sizing:border-box}
html,body{width:900px;height:1200px;overflow:hidden;background:var(--paper)}
body{font-family:"Noto Sans JP",sans-serif;color:var(--ink)}
.flyer{position:relative;width:900px;height:1200px;overflow:hidden;background:var(--paper)}
.backdrop{position:absolute;left:0;top:0;width:900px;height:620px}
.abs{position:absolute}
.vert{writing-mode:vertical-rl;text-orientation:upright}

.catch{left:26px;top:22px;font-size:34px;font-weight:900;line-height:1.3;letter-spacing:1px;white-space:nowrap}
.catch em{font-style:normal;color:var(--green);font-size:42px}

.subcatch{left:612px;top:14px;width:270px;height:110px;background:var(--paper);border:3px solid var(--green);border-radius:55px;
  display:flex;align-items:center;justify-content:center;text-align:center;font-size:16px;font-weight:700;line-height:1.5}

.title-band{left:410px;top:10px;width:200px;height:420px;background:var(--dark);transform:rotate(-12deg);
  display:flex;flex-direction:row-reverse;justify-content:center;align-items:flex-start;gap:10px;padding:24px 0}
.title-band .lead{writing-mode:vertical-rl;text-orientation:upright;font-size:20px;font-weight:900;letter-spacing:3px;
  background:var(--paper);color:var(--green);padding:8px 4px}
.title-band .main{writing-mode:vertical-rl;text-orientation:upright;color:#fff;font-size:28px;font-weight:900;line-height:1.25;letter-spacing:2px}

.device{left:262px;top:132px;width:88px;height:118px;border-radius:8px;background:linear-gradient(160deg,#4a7fc4,#1d3f78)}

.tech-tag{left:30px;top:140px;width:70px;height:220px;background:var(--green);color:#fff;font-size:16px;font-weight:700;
  padding:10px 0;display:flex;justify-content:center;line-height:1.35}
.tech-tag b{color:var(--yellow);font-weight:900}
.speed-tag{left:112px;top:170px;width:58px;height:200px;background:var(--yellow);font-size:15px;font-weight:700;
  display:flex;justify-content:center;padding:8px 0;line-height:1.35}
.talk-left{left:184px;top:140px;font-size:20px;font-weight:900;line-height:1.25;color:var(--dark);letter-spacing:1px}
.talk-left span{color:var(--green)}

.bonus{left:660px;top:150px;width:140px;height:140px;border-radius:50%;background:var(--green);color:#fff;
  display:flex;flex-direction:column;align-items:center;justify-content:center;text-align:center}
.bonus small{font-size:13px;font-weight:700;background:var(--paper);color:var(--green);padding:1px 8px;border-radius:10px}
.bonus strong{font-size:26px;font-weight:900;color:var(--yellow);line-height:1.2;margin:4px 0}
.bonus span{font-size:12px;font-weight:700;line-height:1.3}
.talk-right{left:818px;top:150px;font-size:22px;font-weight:900;line-height:1.25;color:var(--dark);letter-spacing:1px}
.talk-right span{color:var(--green)}

.speaker{font-size:11px;line-height:1.55}
.speaker .photo{flex:none;width:90px;height:105px;background:linear-gradient(180deg,#d9dfe6,#8d98a6)}
.speaker .name{font-size:22px;font-weight:900;letter-spacing:2px;line-height:1.3;margin-bottom:2px}
.speaker .role{font-size:11px;font-weight:500}
.sp-left{left:30px;top:455px;width:440px;display:flex;gap:12px}
.sp-right{left:480px;top:440px;width:400px}
.sp-right .head{display:flex;gap:12px;align-items:flex-start}
.sp-right .bio{margin-top:6px;font-size:10.5px;line-height:1.5}

.schedule{left:0;top:620px;width:900px;height:58px;background:var(--paper);border-top:3px solid var(--dark);display:flex;align-items:center;padding-left:26px;gap:16px}
.schedule .date{font-size:38px;font-weight:900;letter-spacing:-1px}
.schedule .date small{font-size:20px}
.schedule .info{font-size:13px;font-weight:500;line-height:1.45}
.schedule .info b{font-size:16px}
.live{margin-left:auto;height:100%;background:var(--green);color:#fff;padding:0 22px;display:flex;flex-direction:column;justify-content:center;text-align:center}
.live small{font-size:13px;font-weight:700;background:#fff;color:var(--green);padding:0 6px}
.live strong{font-size:22px;font-weight:900}

.apply-bar{left:0;top:678px;width:900px;height:46px;background:var(--green);color:#fff;display:flex;align-items:center;padding-left:26px;gap:18px}
.apply-bar .ttl{font-size:20px;font-weight:900;background:#fff;color:var(--green);padding:2px 10px}
.apply-bar .fax{font-size:30px;font-weight:900;letter-spacing:1px}
.apply-bar .fax small{font-size:18px;margin-right:6px}
.deadline{margin-left:auto;margin-right:26px;display:flex;align-items:center;gap:10px}
.deadline small{font-size:12px;font-weight:700;line-height:1.2}
.deadline strong{font-size:28px;font-weight:900;background:#fff;color:var(--ink);padding:0 10px}

.form{left:26px;top:732px;width:848px;border-collapse:collapse;font-size:14px}
.form th,.form td{border:1px solid var(--line);height:33px;padding:2px 8px;vertical-align:middle}
.form th{background:var(--green-pale);font-weight:700;width:96px;text-align:center}
.form .ruby{height:22px;font-size:10px;color:#666}
.form .sub{background:var(--green-pale);font-weight:700;width:70px;text-align:center;font-size:13px}
.form .note{font-size:11px;line-height:1.5}

.footer{left:26px;top:1112px;width:848px;display:flex;gap:30px;font-size:11px;line-height:1.5}
.footer .lbl{display:inline-block;background:var(--dark);color:#fff;padding:0 8px;font-weight:700;margin-bottom:3px}
.footer .org{font-size:14px;font-weight:700}
.footer .tel{font-size:18px;font-weight:900;line-height:1.3}
</style>
</head>
<body>
<div class="flyer">
  <svg class="backdrop" viewBox="0 0 900 620" aria-hidden="true">
    <polygon points="300,0 420,0 900,430 900,560" fill="var(--green-pale)"/>
    <polygon points="560,0 640,0 900,250 900,330" fill="var(--green-light)"/>
    <polygon points="0,380 0,300 360,620 260,620" fill="var(--green-pale)"/>
  </svg>

  <h1 class="abs catch">揺れにくい地盤には<br><em>価値</em>がある。</h1>

  <p class="abs subcatch">地盤の揺れやすさは、<br>今までの地盤測定方法では<br>計測出来ませんでした。</p>

  <div class="abs title-band">
    <p class="lead">最新工務店戦略</p>
    <h2 class="main">地盤の揺れやすさを知って<br>地震に備えた家づくり</h2>
  </div>

  <div class="abs device" role="img" aria-label="ハイブリッド微動探査の計測機器の写真"></div>

  <p class="abs tech-tag vert">最新技術 <b>ハイブリッド</b><br>微動探査のご紹介</p>
  <p class="abs speed-tag vert">短時間で<br>今まで出来ない精度の測定</p>
  <h3 class="abs talk-left vert">地震大国に必要とされる<br><span>ハイブリット微動探査の将来性</span></h3>

  <div class="abs bonus">
    <small>来場者特典</small>
    <strong>初回調査</strong>
    <span>来場者特別価格<br>にてご提供</span>
  </div>
  <h3 class="abs talk-right vert">地盤の揺れやすさを知った<br><span>家づくりの重要性</span></h3>

  <section class="abs speaker sp-left">
    <div class="photo" role="img" aria-label="講師 浦辺直孝の肖像写真"></div>
    <div>
      <p class="name">浦辺 直孝</p>
      <p class="role">蒼洋材料技術機構 主幹研究員／博士(工学)<br>複層素材耐久分析部門 兼<br>湾岸フロンティア計測センター 主幹研究員</p>
      <p>2017年4月9日TVRドキュメント<br>「森の湖 あの町はどこへ?~消えゆく“水辺の記憶”~」<br>新聞・雑誌等掲載多数</p>
    </div>
  </section>

  <section class="abs speaker sp-right">
    <div class="head">
      <div class="photo" role="img" aria-label="講師 宮下航の肖像写真"></div>
      <div>
        <p class="name">宮下 航</p>
        <p class="role">株式会社Tk’s空間計画 代表取締役社長<br>「匠研舎」塾長<br>一級建築士、一級構造建築士<br>専門は木造構造建築物の構造設計・構造計算</p>
      </div>
    </div>
    <p class="bio">工務店を経て、2006年5月㈱Tk‘s空間計画を設立、2010年1月「匠研舎」を設立し、木質構造に関するセミナーや構造計算技術者育成を行っている。現在は「匠研舎」の講座をweb化した「匠研舎チャンネル」、Cliporaにて情報発信中。著書に「すっきり学べる!石積み読本」がある。</p>
  </section>

  <div class="abs schedule">
    <p class="date">6月23日<small>(水)</small></p>
    <p class="info"><b>14:00~16:00</b>(受付開始13:30)<br>刈谷市北部市民交流ホール5階(501~503)</p>
    <p class="info">定員<br><b>50名</b></p>
    <div class="live"><small>同時開催</small><strong>Vidora LIVE配信</strong></div>
  </div>

  <div class="abs apply-bar">
    <span class="ttl">セミナー申込書</span>
    <span class="fax"><small>FAX</small>01-2345-6789</span>
    <div class="deadline"><small>お申込み<br>締切日</small><strong>4月18日(日)</strong></div>
  </div>

  <table class="abs form">
    <tr><th rowspan="2">会社名</th><td class="ruby" colspan="5">フリガナ</td></tr>
    <tr><td colspan="5"></td></tr>
    <tr><th>ご住所</th><td colspan="5">〒</td></tr>
    <tr><th rowspan="4">参加者名</th><td class="ruby">フリガナ</td><td class="sub" rowspan="2">部署名</td><td rowspan="2"></td><td class="sub" rowspan="2">役職名</td><td rowspan="2"></td></tr>
    <tr><td></td></tr>
    <tr><td class="ruby">フリガナ</td><td class="sub" rowspan="2">部署名</td><td rowspan="2"></td><td class="sub" rowspan="2">役職名</td><td rowspan="2"></td></tr>
    <tr><td></td></tr>
    <tr><th rowspan="2">ご連絡先</th><td colspan="2">TEL</td><td class="sub">FAX</td><td colspan="2"></td></tr>
    <tr><td colspan="5">E-mail</td></tr>
    <tr><th>参加人数</th><td>　　　　　　名</td><td class="sub">参加方法</td><td colspan="3">□ 現地　　□ WEB</td></tr>
    <tr><td colspan="6" class="note">※WEBでご参加の場合はE-mailを必ずご記入下さい。　※会場入場前にご名刺を1枚頂戴いたしますのでご準備ください。</td></tr>
  </table>

  <footer class="abs footer">
    <div>
      <span class="lbl">主催</span>
      <p class="org">株式会社R-VANTLO</p>
      <p>〒471-0835愛知県名古屋市中区桜庭二丁目8番4号‐705号<br>URL:https://rvantlo-example.co.jp/</p>
    </div>
    <div>
      <span class="lbl">協賛</span>
      <p>一般社団法人蒼岳地層調査会<br>一般社団法人ソルベン<br>株式会社タカミネ</p>
    </div>
    <div>
      <span class="lbl">お問い合わせ</span>
      <p>株式会社R-VANTLO 担当 村瀬</p>
      <p class="tel">080-2938-6074</p>
      <p>murase-hideaki@rvantlo-example.co.jp</p>
    </div>
  </footer>
</div>
</body>
</html>
```